Tolvern Business Cards

Business card design. dont mind if new logo is suggested.
it would be for a security company.
our clients would be bigger security companies around Australia.
have a logo done but can be replaced. see attaached. like the colors.
Need company name, person name, designation, phone and email on front.
At back company logo and name. website saddress and 2 x license numbers
would like to have 2 different background color for both sidde

Industry/Entity Type

Security

Contact Information for Business Card

round corners, front should be light in color. need logo at back with webaddress and 2 x license numners

Font styles to use
Sans Serif

Colors
f37122
faa54b
f8ba93
0255a3
0592cd
85cae6
b3d448
9bcb3c
ffffff

Requirements
Must have
• see description
Nice to have
• see description
Should not have
• should not be difficult to read or hardd to find information on card.. lets say easy on eyes yet catchy

```html
<!DOCTYPE html>
<html lang="en">
<head>
<meta charset="utf-8">
<title>Tolvern Business Cards</title>
<link rel="stylesheet" href="https://fonts.googleapis.com/css2?family=Open+Sans:wght@400;600;700&display=swap">
<style>
  :root {
    --stage: #e9ebee;
    --card-white: #ffffff;
    --card-back: #f4f5f6;
    --navy: #1d3f73;
    --cyan: #0592cd;
    --text-grey: #4a4d52;
    --soft-grey: #8a8d92;
    --dot-blue: #cde6ee;
    --dot-grey: #d7dbe0;
    --shadow: rgba(20, 28, 40, 0.18);
  }
  * { box-sizing: border-box; margin: 0; padding: 0; }
  html, body {
    width: 1200px;
    height: 960px;
    overflow: hidden;
    background: var(--stage);
    font-family: "Open Sans", sans-serif;
  }
  .canvas {
    position: relative;
    width: 1200px;
    height: 960px;
  }
  .card {
    position: absolute;
    width: 700px;
    height: 400px;
    border-radius: 14px;
    overflow: hidden;
    box-shadow: 0 10px 30px var(--shadow);
  }

  /* Back side */
  .card-back {
    left: 400px;
    top: 60px;
    background: var(--card-back);
  }
  .brand {
    position: absolute;
    left: 0;
    right: 0;
    top: 130px;
    text-align: center;
  }
  .brand-mark {
    display: block;
    width: 74px;
    height: 74px;
    margin: 0 auto 18px;
    border-radius: 50%;
    background: var(--cyan);
  }
  .brand-name {
    font-size: 26px;
    font-weight: 700;
    letter-spacing: 0.5px;
    color: var(--navy);
    text-transform: uppercase;
  }
  .brand-web {
    margin-top: 4px;
    font-size: 17px;
    letter-spacing: 9px;
    color: var(--navy);
  }
  .licences {
    position: absolute;
    left: 0;
    right: 0;
    bottom: 32px;
    text-align: center;
    font-size: 17px;
    color: var(--soft-grey);
  }
  .licences .divider { margin: 0 10px; }

  /* Front side */
  .card-front {
    left: 120px;
    top: 500px;
    background: var(--card-white);
  }
  .front-pattern {
    position: absolute;
    inset: 0;
    width: 100%;
    height: 100%;
  }
  .contact {
    position: absolute;
    left: 300px;
    top: 112px;
    color: var(--text-grey);
    font-size: 18px;
    line-height: 1.3;
  }
  .person-name {
    font-size: 24px;
    font-weight: 700;
    color: var(--navy);
    letter-spacing: 0.3px;
    margin-left: 60px;
  }
  .person-role {
    font-size: 20px;
    color: var(--cyan);
    margin-left: 60px;
    margin-bottom: 10px;
  }
  .address { margin-bottom: 10px; }
  .phone { margin-left: 10px; }
</style>
</head>
<body>
  <main class="canvas">

    <section class="card card-back" aria-label="Back of business card">
      <div class="brand">
        <span class="brand-mark" aria-hidden="true"></span>
        <div class="brand-name">Tolvern Security Group</div>
        <div class="brand-web">www.tolvern.com</div>
      </div>
      <p class="licences">Lic No. #40213386<span class="divider">|</span>#71590245</p>
    </section>

    <section class="card card-front" aria-label="Front of business card">
      <svg class="front-pattern" viewBox="0 0 700 400" preserveAspectRatio="none"
           role="img" aria-label="Soft pattern of light blue and grey dots across the card">
        <defs>
          <linearGradient id="dot-field" x1="0" y1="0" x2="1" y2="1">
            <stop offset="0" stop-color="#cde6ee" stop-opacity="0.75"/>
            <stop offset="0.5" stop-color="#f4f6f8" stop-opacity="0.6"/>
            <stop offset="1" stop-color="#d7dbe0" stop-opacity="0.9"/>
          </linearGradient>
        </defs>
        <rect width="700" height="400" fill="url(#dot-field)"/>
      </svg>
      <div class="contact">
        <div class="person-name">DANIEL REYES</div>
        <div class="person-role">CEO/FOUNDER</div>
        <div class="address">4120 Larkfield Road<br>Ballarat, Victoria 3350</div>
        <div class="phone">612 555 0184</div>
        <div class="email">daniel@tolvern.com</div>
        <div class="web">www.tolvern.com</div>
      </div>
    </section>

  </main>
</body>
</html>
```